Northern Summit Builders & Affiliates Redesigning our Look

We need stationary (letterhead, envelopes, notepads, invoicing templates, etc) that all coordinate. We are an commerial and residential exteriors construction company that operates 3 companies which all run exclusively, however, the compliment one another well.

Northern Summit Builders (this company installs exteriors on jobsites both residential and commercial)
Northern Summit Roofing & Building Supply (this company sells exterior building materials to homeowners and builders.)
Northern Summit Dumpster Services (This company delivers roll away dumpster cans to homeowners and builders)

Just a note: When I say we do exterior work. We do roofing, siding, stone, windows/doors, gutters, and decks.

We are looking for stationary that includes all three and keeps with our patriotic theme

Info on our firm:
Address: 2718 Tamarind Rd, Elkton MI 48512
Phone: 231-555-0172
Website: www.northernsummit-example.us

Target Market(s)

Our companies target market is vast. We work in the B2B space as well as with homeowner (retail customers). We are in the home and commercial buiding construction field. We specialized in exteriors. (Roofing, Siding, Stone, Windows, Doors, Decks, Gutters)

Industry/Entity Type

Construction

Colors
ec1f27
ffffff
0555a3

Requirements
Must have
• Would like to have a clean professional look with a patriotic theme
Nice to have
• Red/White/Blue

```html
<!DOCTYPE html>
<html lang="en">
<head>
<meta charset="utf-8">
<title>Northern Summit Builders – Business Cards</title>
<link rel="stylesheet" href="https://fonts.googleapis.com/css2?family=Questrial&family=Josefin+Sans:wght@700&display=swap">
<style>
  :root {
    --navy: #14174a;
    --red: #e01f26;
    --paper: #f1f2f4;
    --ink: #1b1b1f;
    --ground: #dcdcec;
    --muted: #c8cad8;
    --flag-blue: #1c2160;
  }
  * { margin: 0; padding: 0; box-sizing: border-box; }
  html, body { width: 1200px; height: 906px; overflow: hidden; }
  body {
    background: var(--ground);
    font-family: "Questrial", "Century Gothic", sans-serif;
    position: relative;
  }
  .card {
    position: absolute;
    top: 299px;
    width: 540px;
    height: 308px;
    box-shadow: 0 6px 18px rgba(40, 40, 80, 0.18);
  }
  .card--back { left: 40px; background: var(--navy); color: #fff; }
  .card--front { left: 620px; background: var(--paper); color: var(--ink); }

  .brand {
    position: absolute;
    font-family: "Josefin Sans", "Questrial", sans-serif;
    font-weight: 700;
    font-size: 34px;
    line-height: 1;
    letter-spacing: 0.5px;
  }
  .card--back .brand { left: 36px; top: 112px; color: #fff; }
  .card--front .brand { left: 40px; top: 152px; color: var(--ink); }
  .brand span { display: block; }
  .brand span + span { margin-left: 36px; margin-top: 4px; }

  .brand-flag {
    position: absolute;
    border-radius: 3px 40px 40px 3px;
  }
  .card--back .brand-flag {
    left: 200px; top: 132px; width: 150px; height: 48px;
    background: linear-gradient(180deg, #e8e9f0 0%, #b9bccd 100%);
  }
  .card--front .brand-flag {
    left: 205px; top: 160px; width: 130px; height: 46px;
    background: linear-gradient(90deg, var(--flag-blue) 0 35%, var(--red) 35% 100%);
  }

  .divisions {
    position: absolute;
    right: 28px; top: 44px;
    list-style: none;
    text-align: right;
  }
  .division {
    position: relative;
    padding-right: 16px;
    margin-bottom: 16px;
    font-size: 12px;
    line-height: 1.25;
  }
  .division::after {
    content: "";
    position: absolute;
    right: 0; top: 2px;
    width: 3px; height: 24px;
    background: var(--red);
  }
  .division strong { font-family: "Josefin Sans", sans-serif; font-weight: 700; display: block; font-size: 12px; }
  .division span { color: var(--muted); letter-spacing: 0.5px; }

  .website {
    position: absolute;
    right: 44px; bottom: 44px;
    font-size: 12px;
    letter-spacing: 1px;
  }
  .website em { font-style: normal; color: var(--red); }

  .flag-art {
    position: absolute;
    right: 34px; top: 18px;
    width: 300px; height: 170px;
    border-radius: 40px 6px 80px 10px;
    background: linear-gradient(90deg, var(--flag-blue) 0 42%, var(--red) 42% 100%);
    opacity: 0.95;
  }

  .person {
    position: absolute;
    left: 54px; bottom: 40px;
  }
  .person-name {
    font-family: "Josefin Sans", sans-serif;
    font-weight: 700;
    font-size: 17px;
    letter-spacing: 1px;
  }
  .person-role { font-size: 13px; margin-top: 2px; }

  .location {
    position: absolute;
    bottom: 40px;
    padding-left: 12px;
    border-left: 3px solid var(--red);
    font-size: 11.5px;
    line-height: 1.35;
  }
  .location--elkton { left: 254px; }
  .location--lakeview { left: 398px; }
  .location b { color: var(--red); font-weight: 400; }
</style>
</head>
<body>
  <section class="card card--back" aria-label="Card back">
    <div class="brand"><span>Northern</span><span>Summit</span></div>
    <div class="brand-flag" role="img" aria-label="Brushed flag illustration beside the name"></div>
    <ul class="divisions">
      <li class="division"><strong>Northern Summit</strong><span>Builders</span></li>
      <li class="division"><strong>Northern Summit</strong><span>Roofing &amp; Building Supply</span></li>
      <li class="division"><strong>Northern Summit</strong><span>Dumpster Services</span></li>
    </ul>
    <p class="website">www.<em>northernsummit-example</em>.us</p>
  </section>

  <section class="card card--front" aria-label="Card front">
    <div class="flag-art" role="img" aria-label="Large distressed American flag illustration"></div>
    <div class="brand"><span>Northern</span><span>Summit</span></div>
    <div class="brand-flag" role="img" aria-label="Small brushed flag illustration beside the name"></div>
    <div class="person">
      <p class="person-name">JORDAN WHITFIELD</p>
      <p class="person-role">General Manager</p>
    </div>
    <address class="location location--elkton" style="font-style:normal">
      2718 Tamarind Rd<br>Elkton MI 48512<br><b>T:</b> 231-555-0172
    </address>
    <address class="location location--lakeview" style="font-style:normal">
      4460 Birchwood Road<br>Lakeview MI 48850<br><b>T:</b> 844.555.0198
    </address>
  </section>
</body>
</html>
```